Tall Maple website Laser Like Lipo and Facial Rejuvenation busines

I need a website for my Laser Like Lipo and Facial Rejuvenation business called Tall Maple. I purchased the domain name. I have a logo and before and after pictures to include along with basic information about the procedure and pricing information. I would like my website to be used by customers to be able to schedule appointments. My logo and before-and-after pictures are attached.

My business is called Tall Maple. It is a laser like Lipo and facial rejuvenation. I've attached my logo and before and after pictures to use on the website.

These treatments are non invasive and people lose 2-10 inches per treatment. My primary audience will be overweight women 30 years of age or older or those with cellulite. I will have some male customers too but mostly women.

As for the web design, I've never had a website before so I really don't have anything specific in mind. I'm open to considering anything. I'm not a girly, girl and I don't like frilly, fancy stuff. I just want something simple but not to either. I love my logo. That is a great fit for my business and personality. I have increased the budget to include coding.

I do not like pastel colors. I do need colors that compliment my logo.

Target Market(s)

Mostly over weight Women or those with cellulite ages 30 and above. Some men.

Industry/Entity Type

Business

Coding

Coded - Design and coding required

Number of Pages Required

3 page

Font styles to use
Serif

Requirements
Must have
• I want my logo and information section on one page, a page for before and after pictures that enlarge when clicked on. I do not want a slide show, and a page for prices. I previously mentioned a section for them to schedule appointments but have decided that I don't want that.
• I do not like pastel colors. I do need colors that compliment my logo.
Should not have
• Not a slide show

```html
<!DOCTYPE html>
<html lang="en">
<head>
<meta charset="utf-8">
<title>Tall Maple – Laser Like Lipo &amp; Facial Rejuvenation</title>
<link href="https://fonts.googleapis.com/css2?family=Oswald:wght@400;500;600&family=Open+Sans:wght@400;600;700&display=swap" rel="stylesheet">
<style>
:root{
  --red:#c4161c;
  --red-dark:#8e0c10;
  --ink:#222;
  --muted:#666;
  --dark:#1c1c1c;
  --grey:#e6e6e6;
  --white:#fff;
}
*{box-sizing:border-box;margin:0;padding:0}
html,body{width:820px;height:1200px;overflow:hidden;background:var(--white)}
body{font-family:"Open Sans",Arial,sans-serif;color:var(--ink)}
.page{width:820px;height:1200px;position:relative}

/* header */
.site-header{height:80px;display:flex;align-items:center;justify-content:space-between;padding:0 40px 0 90px}
.brand{display:flex;align-items:center;gap:8px}
.brand-mark{width:14px;height:14px;border-radius:50%;background:var(--red)}
.brand-name{font-family:"Open Sans",Arial,sans-serif;font-weight:700;font-size:22px;color:var(--red-dark)}
.main-nav{display:flex;gap:22px}
.main-nav a{font-size:10px;font-weight:600;color:#555;text-decoration:none;text-transform:uppercase}
.main-nav a.active{color:var(--red)}

/* hero */
.hero{height:300px;background:radial-gradient(ellipse at 40% 50%,#d8252b 0%,var(--red) 45%,var(--red-dark) 100%);position:relative;display:flex;align-items:center;padding:0 0 0 90px}
.hero-title{font-family:"Oswald",Arial,sans-serif;color:var(--white);text-transform:uppercase;line-height:1.05}
.hero-title .small{display:block;font-size:38px;font-weight:500}
.hero-title .big{display:block;font-size:66px;font-weight:600;line-height:1}
.hero-title .mid{display:block;font-size:36px;font-weight:500}
.hero-photo{position:absolute;right:90px;top:40px;width:270px;height:200px;border:6px solid var(--white);background:linear-gradient(135deg,#f3e6dc 0%,#e7cbb8 50%,#cfa58b 100%);box-shadow:0 4px 12px rgba(0,0,0,.35)}

/* intro band */
.intro-band{height:110px;background:linear-gradient(#333,var(--dark));display:flex;align-items:center;justify-content:space-between;padding:0 90px}
.intro-band p{font-size:12px;font-style:italic;color:#ddd;max-width:400px;line-height:1.5}
.btn{display:inline-block;background:var(--red);color:var(--white);font-weight:700;font-size:12px;text-transform:uppercase;padding:11px 18px;border-radius:3px;text-decoration:none}

/* welcome */
.welcome{height:220px;text-align:center;padding:28px 90px 0}
.section-title{font-family:"Oswald",Arial,sans-serif;font-weight:500;font-size:30px;text-transform:uppercase;color:var(--ink)}
.rule{width:60px;height:3px;background:var(--red);margin:8px auto 14px}
.welcome p{font-size:8px;line-height:1.6;color:var(--muted);text-align:left;margin-bottom:16px}

/* results */
.results{height:330px;background:var(--grey);text-align:center;padding-top:24px}
.results .section-title{color:var(--red)}
.results .lead{font-size:15px;font-weight:600;color:var(--ink);margin:4px 0 22px}
.cards{display:flex;justify-content:center;gap:22px}
.card{width:190px;background:#111;border-radius:4px;padding:8px 8px 12px}
.card-photos{display:flex;gap:4px;height:80px}
.card-photo{flex:1;position:relative;background:linear-gradient(160deg,#d9c3b4,#a88571)}
.card-photo span{position:absolute;left:4px;top:3px;font-size:8px;color:var(--white)}
.card h3{font-weight:400;font-size:15px;color:var(--white);margin:12px 0 10px}
.card .btn{font-size:12px;text-transform:none;padding:6px 14px;font-weight:600}

/* footer */
.site-footer{height:160px;display:flex;gap:30px;padding:22px 40px 0 70px}
.foot-brand{width:150px}
.foot-brand .brand-name{font-size:18px}
.foot-brand small{display:block;font-size:7px;color:var(--muted);margin-top:6px}
.foot-col{width:110px}
.foot-col.location{width:140px}
.foot-col h4{font-size:8px;font-weight:700;color:var(--red);text-transform:uppercase;margin-bottom:6px}
.foot-col a{display:block;font-size:8px;color:#444;text-decoration:none;line-height:1.6}
.map{width:130px;height:80px;background:linear-gradient(135deg,#eee8dc,#dcd6c8);border:1px solid #ccc}
</style>
</head>
<body>
<div class="page">
  <header class="site-header">
    <div class="brand"><span class="brand-mark"></span><span class="brand-name">Tall Maple</span></div>
    <nav class="main-nav">
      <a class="active" href="#">Home</a><a href="#">About Us</a><a href="#">Before &amp; After</a><a href="#">Prices</a><a href="#">Contact Us</a>
    </nav>
  </header>

  <section class="hero">
    <h1 class="hero-title">
      <span class="small">We provide laser</span>
      <span class="small">like lipo and</span>
      <span class="big">Facial</span>
      <span class="mid">Rejuvenation</span>
    </h1>
    <div class="hero-photo" role="img" aria-label="Portrait photo of a woman with smooth skin"></div>
  </section>

  <section class="intro-band">
    <p>Lorem Ipsum is simply dummy text of the printing and typesetting industry. Lorem Ipsum has been the industry's standard dummy text ever</p>
    <a class="btn" href="#">View Our Prices</a>
  </section>

  <section class="welcome">
    <h2 class="section-title">Welcome to Tall Maple</h2>
    <div class="rule"></div>
    <p>Tall Maple offers laser like lipo and facial rejuvenation treatments in a calm, private studio. Each session is non invasive, needs no downtime and is planned around your goals. Our clients lose between two and ten inches per treatment while skin looks firmer and smoother. We welcome women and men who want real results without surgery, and we keep every visit simple, friendly and focused on you.</p>
    <a class="btn" href="#">Contact Us</a>
  </section>

  <section class="results">
    <h2 class="section-title">Before &amp; After Treatments</h2>
    <p class="lead">These treatments are non invasive and people Lose 2-10 Inches Per Treatment</p>
    <div class="cards">
      <article class="card">
        <div class="card-photos">
          <div class="card-photo" role="img" aria-label="Back view before treatment"><span>Before</span></div>
          <div class="card-photo" role="img" aria-label="Back view after treatment"><span>After</span></div>
        </div>
        <h3>1 laser like Lipo</h3>
        <a class="btn" href="#">Treatment</a>
      </article>
      <article class="card">
        <div class="card-photos">
          <div class="card-photo" role="img" aria-label="Waist before treatment"><span>Before</span></div>
          <div class="card-photo" role="img" aria-label="Waist after treatment"><span>After</span></div>
        </div>
        <h3>1 laser like Lipo</h3>
        <a class="btn" href="#">Treatment</a>
      </article>
      <article class="card">
        <div class="card-photos">
          <div class="card-photo" role="img" aria-label="Abdomen before treatment"><span>Before</span></div>
          <div class="card-photo" role="img" aria-label="Abdomen after treatment"><span>After</span></div>
        </div>
        <h3>8 laser like Lipo</h3>
        <a class="btn" href="#">Treatment</a>
      </article>
    </div>
  </section>

  <footer class="site-footer">
    <div class="foot-brand">
      <div class="brand"><span class="brand-mark"></span><span class="brand-name">Tall Maple</span></div>
      <small>Laser Like Lipo</small>
    </div>
    <div class="foot-col">
      <h4>Quick Links</h4>
      <a href="#">Home</a><a href="#">About us</a><a href="#">Before &amp; After</a><a href="#">Prices</a><a href="#">Contact Us</a>
    </div>
    <div class="foot-col">
      <h4>Other Links</h4>
      <a href="#">Terms &amp; Conditions</a><a href="#">Privacy Policy</a>
    </div>
    <div class="foot-col location">
      <h4>Location</h4>
      <div class="map" role="img" aria-label="Street map showing the studio location"></div>
    </div>
    <div class="foot-col">
      <h4>Get in Touch</h4>
      <a href="#">Facesheet</a><a href="#">Chirper</a>
    </div>
  </footer>
</div>
</body>
</html>
```